"Autumn Special" 6 Month Membership Special

Running a Membership Drive on a 6 month membership option for the month of April/May. 6 months $150.00 save 50%. Below is recent ads made from designers on Vellum Forge to assist. Final design should be inviting / colorful and eye catching

Format required is for a Facebook cover, Instagram, and A0 format for a poster .

Target Market(s)

16-40 male and female

Industry/Entity Type

Fitness

Font styles to use
Serif
Other font styles liked:
• Athletic

Colors

Designer to choose colors to be used in the design.

Requirements
Must have
• The main emphasis would be on the "6 MONTH SPECIAL" or "AUTUMN SPECIAL" font/text (special) and the layout of the text. If we can add some brighter colors to the layout that would be great just to capture their attention. If there's any effects you want to add to it that would be great. The logo can be faint in the background. The image of the female model can some some artistic effects around it and she does not have to be the main focus
• "AUTUMN SPECIAL"
• 6 MONTHS from
• $150.00
• SAVE 50%"
• "Terms and conditions apply"
• All contact details, address, website, etc which will be supplied
Nice to have
• Some artistic effects to catch your eye and enhance the professionalism of the designer. Attached is a "Athletic font" Logo which that style could be incorporated
Should not have
• You don't have to include the orange background of the female model, you can use her silhouette

```html
<!DOCTYPE html>
<html lang="en">
<head>
<meta charset="utf-8">
<title>Autumn Special – Stride Fitness Hall</title>
<link rel="stylesheet" href="https://fonts.googleapis.com/css2?family=Alfa+Slab+One&family=Oswald:wght@600&family=PT+Sans+Narrow&display=swap">
<style>
  :root {
    --red: #e23c1e;
    --slate: #9aacb8;
    --ink: #1f1f1f;
    --paper: #f2f4f5;
    --stage: #ffffff;
    --blue: #4e6591;
    --orange: #e88a5a;
    --mist: #dfe7ee;
  }
  * { margin: 0; padding: 0; box-sizing: border-box; }
  html, body { width: 1200px; height: 986px; overflow: hidden; background: var(--stage); }
  .stage { position: relative; width: 1200px; height: 986px; }

  .piece {
    position: absolute;
    background: var(--paper);
    border: 1px solid #e4e6e8;
    box-shadow: 0 6px 22px rgba(0,0,0,.08);
    overflow: hidden;
  }
  .piece > * { position: absolute; line-height: 1; }

  .cover { left: 44px; top: 112px; width: 432px; height: 200px; }
  .square { left: 48px; top: 426px; width: 428px; height: 427px; }
  .poster { left: 531px; top: 53px; width: 617px; height: 870px; }

  .athlete-photo {
    background:
      radial-gradient(ellipse at 65% 30%, rgba(232,138,90,.85) 0 22%, transparent 45%),
      radial-gradient(ellipse at 40% 55%, var(--blue) 0 35%, transparent 62%),
      radial-gradient(ellipse at 55% 80%, rgba(120,140,180,.6) 0 30%, transparent 60%);
    border-radius: 40% 50% 45% 40%;
  }

  .headline-top, .headline-bottom {
    font-family: "Alfa Slab One", serif;
    text-align: center;
    letter-spacing: 1px;
  }
  .headline-top { color: var(--red); }
  .headline-bottom { color: var(--slate); }
  .headline-rule { height: 1.5px; background: var(--slate); }

  .brand-name {
    font-family: "Oswald", sans-serif;
    font-weight: 600;
    color: var(--slate);
    text-align: center;
    text-transform: uppercase;
  }
  .brand-name span { display: block; }

  .offer { font-family: "Oswald", sans-serif; font-weight: 600; color: var(--red); white-space: nowrap; }
  .offer sup { font-size: .5em; vertical-align: top; position: relative; top: .1em; }
  .offer-label { font-family: "Alfa Slab One", serif; color: var(--slate); font-weight: 400; }
  .offer-stacked { display: inline-block; text-align: right; line-height: 1; vertical-align: top; }

  .small-print, .contact, .web {
    font-family: "PT Sans Narrow", sans-serif;
    color: var(--ink);
    text-align: center;
    white-space: nowrap;
  }

  /* cover */
  .cover .athlete-photo { left: 4px; top: 0; width: 172px; height: 200px; }
  .cover .brand-name { left: 248px; top: 17px; width: 120px; font-size: 20px; }
  .cover .brand-name span + span { font-size: 7px; letter-spacing: 3px; margin-top: 2px; }
  .cover .headline-top { left: 196px; top: 68px; width: 220px; font-size: 30px; }
  .cover .headline-rule { left: 196px; top: 95px; width: 220px; }
  .cover .headline-bottom { left: 196px; top: 98px; width: 220px; font-size: 31px; }
  .cover .offer { left: 222px; top: 133px; width: 184px; font-size: 22px; }
  .cover .offer .offer-stacked { font-size: 8px; margin-top: 3px; }
  .cover .offer .offer-save { font-size: 8px; }
  .cover .small-print { left: 196px; top: 168px; width: 220px; font-size: 7px; }
  .cover .web { left: 196px; top: 178px; width: 220px; font-size: 11px; }

  /* square */
  .square .athlete-photo { left: 0; top: 26px; width: 192px; height: 372px; }
  .square .brand-name { left: 220px; top: 54px; width: 140px; font-size: 30px; }
  .square .brand-name span + span { font-size: 9px; letter-spacing: 4px; margin-top: 3px; }
  .square .contact { left: 200px; width: 180px; font-size: 10px; }
  .square .contact-address { top: 107px; }
  .square .contact-email { top: 119px; }
  .square .headline-top { left: 176px; top: 172px; width: 232px; font-size: 38px; }
  .square .headline-rule { left: 176px; top: 203px; width: 232px; }
  .square .headline-bottom { left: 176px; top: 205px; width: 232px; font-size: 38px; }
  .square .offer-months { left: 206px; top: 252px; font-size: 34px; }
  .square .offer-months .offer-stacked { font-size: 14px; margin-top: 2px; }
  .square .offer-save { left: 270px; top: 292px; font-size: 32px; }
  .square .offer-save .offer-label { font-size: 14px; }
  .square .small-print { left: 150px; top: 354px; width: 230px; font-size: 10px; }
  .square .web { left: 150px; top: 372px; width: 230px; font-size: 15px; }

  /* poster */
  .poster .headline-top { left: 0; top: 88px; width: 617px; font-size: 70px; letter-spacing: 3px; }
  .poster .headline-rule { left: 61px; top: 149px; width: 484px; height: 2px; }
  .poster .headline-bottom { left: 0; top: 150px; width: 617px; font-size: 72px; letter-spacing: 3px; }
  .poster .athlete-photo { left: 57px; top: 219px; width: 296px; height: 472px; }
  .poster .offer-stack { left: 378px; top: 252px; width: 200px; }
  .poster .offer-stack > div { line-height: 1; }
  .poster .big-figure { font-size: 92px; }
  .poster .offer-stack .offer-label { font-size: 31px; }
  .poster .offer-stack .gap { margin-top: 6px; }
  .poster .brand-glow {
    left: 160px; top: 620px; width: 300px; height: 130px;
    background: radial-gradient(ellipse, var(--mist) 0 45%, transparent 72%);
  }
  .poster .brand-name { left: 160px; top: 638px; width: 300px; font-size: 64px; color: #fff; }
  .poster .brand-name span + span { font-size: 20px; letter-spacing: 10px; margin-top: 4px; }
  .poster .small-print { left: 0; top: 755px; width: 617px; font-size: 21px; }
  .poster .contact { left: 0; top: 786px; width: 617px; font-size: 20px; }
  .poster .web { left: 0; top: 810px; width: 617px; font-size: 25px; }
</style>
</head>
<body>
<main class="stage">

  <section class="piece cover" aria-label="Facebook cover">
    <div class="athlete-photo" role="img" aria-label="Female athlete running with dumbbells over blue and orange paint strokes"></div>
    <div class="brand-name"><span>Stride</span><span>Fitness Hall</span></div>
    <div class="headline-top">AUTUMN</div>
    <div class="headline-rule"></div>
    <div class="headline-bottom">SPECIAL</div>
    <div class="offer">6<span class="offer-label offer-stacked">MONTHS<br>from $</span>150<sup>00</sup> <span class="offer-label offer-save">SAVE</span> 50<sup>%</sup></div>
    <div class="small-print">Terms and conditions apply</div>
    <div class="web">www.stridegym.com.au</div>
  </section>

  <section class="piece square" aria-label="Instagram post">
    <div class="athlete-photo" role="img" aria-label="Female athlete running with dumbbells over blue and orange paint strokes"></div>
    <div class="brand-name"><span>Stride</span><span>Fitness Hall</span></div>
    <div class="contact contact-address">14 Elm St Riverbend &nbsp; 9000 1234</div>
    <div class="contact contact-email">stridegym@mail.com.au</div>
    <div class="headline-top">AUTUMN</div>
    <div class="headline-rule"></div>
    <div class="headline-bottom">SPECIAL</div>
    <div class="offer offer-months">6 <span class="offer-label offer-stacked">MONTHS<br>from $</span>150<sup>00</sup></div>
    <div class="offer offer-save"><span class="offer-label">SAVE</span> 50<sup>%</sup></div>
    <div class="small-print">Terms and conditions apply</div>
    <div class="web">www.stridegym.com.au</div>
  </section>

  <section class="piece poster" aria-label="A0 poster">
    <div class="headline-top">AUTUMN</div>
    <div class="headline-rule"></div>
    <div class="headline-bottom">SPECIAL</div>
    <div class="athlete-photo" role="img" aria-label="Female athlete running with dumbbells over blue, orange and green paint strokes"></div>
    <div class="offer offer-stack">
      <div class="big-figure">6</div>
      <div class="offer-label">MONTHS</div>
      <div class="offer-label">from $</div>
      <div class="big-figure gap">150<sup>00</sup></div>
      <div class="offer-label gap">SAVE %</div>
      <div class="big-figure">50</div>
    </div>
    <div class="brand-glow"></div>
    <div class="brand-name"><span>Stride</span><span>Fitness Hall</span></div>
    <div class="small-print">Terms and conditions apply</div>
    <div class="contact">14 Elm St Riverbend &nbsp; 9000 1234 &nbsp; stridegym@mail.com.au</div>
    <div class="web">www.stridegym.com.au</div>
  </section>

</main>
</body>
</html>
```